Business Card Layout for a Staffing Company
Brightmoor Consulting Group
Simple
Mark Dellinger
President
27 Quillhaven Road, Suite 410
Port Washington, New York 11783
mdellinger@brightmoorconsulting.com
brightmoorconsulting.com

```html
<!DOCTYPE html>
<html lang="en">
<head>
<meta charset="utf-8">
<title>Brightmoor Consulting Group — Stationery</title>
<link href="https://fonts.googleapis.com/css2?family=Cinzel:wght@500&family=Open+Sans:wght@400&display=swap" rel="stylesheet">
<style>
  :root {
    --teal: #0e7a63;
    --teal-dark: #095c4a;
    --grey: #b9bcbc;
    --paper: #ffffff;
    --ink: #6b6f6f;
    --bg: #ffffff;
  }
  html, body { margin: 0; padding: 0; overflow: hidden; }
  body { width: 1200px; height: 936px; background: var(--bg); position: relative; font-family: "Open Sans", sans-serif; }
  .sheet { position: absolute; background: var(--paper); box-shadow: 0 2px 8px rgba(0,0,0,.18); overflow: hidden; }
  .sheet svg.swoosh { position: absolute; top: 0; right: 0; }
  .brand { font-family: "Cinzel", serif; font-weight: 500; color: var(--teal); white-space: nowrap; }
  .dot { display: inline-block; border-radius: 50%; background: var(--teal); vertical-align: middle; }
  .small { color: var(--ink); line-height: 1.5; }

  .letterhead { left: 178px; top: 56px; width: 400px; height: 548px; }
  .letterhead .header { position: absolute; left: 22px; top: 26px; display: flex; align-items: center; gap: 8px; }
  .letterhead .brand { font-size: 12px; }
  .letterhead .faint-circle { position: absolute; left: 125px; top: 200px; width: 150px; height: 150px; border-radius: 50%; background: radial-gradient(circle at 40% 40%, #e9f3f0, #d7e8e3); }
  .letterhead .contact { position: absolute; left: 22px; bottom: 30px; font-size: 5.5px; }

  .folder { left: 637px; top: 38px; width: 423px; height: 583px; }
  .folder .lockup { position: absolute; left: 40px; right: 40px; top: 215px; text-align: center; }
  .folder .dot { width: 64px; height: 64px; display: block; margin: 0 auto 16px; }
  .folder .brand { font-size: 26px; line-height: 1.25; white-space: normal; display: block; }

  .card { left: 38px; width: 198px; height: 92px; }
  .card-front { top: 669px; }
  .card-front .header { position: absolute; left: 10px; top: 12px; display: flex; align-items: center; gap: 4px; }
  .card-front .brand { font-size: 7px; }
  .card-front .dot { width: 8px; height: 8px; }
  .card-front .details { position: absolute; left: 10px; top: 34px; font-size: 4.6px; }
  .card-front .web { position: absolute; left: 10px; bottom: 6px; font-size: 4.6px; color: var(--ink); }
  .card-back { top: 784px; background: linear-gradient(135deg, var(--teal) 0%, var(--teal-dark) 100%); }
  .card-back .faint-circle { position: absolute; left: 74px; top: 21px; width: 50px; height: 50px; border-radius: 50%; background: rgba(255,255,255,.14); }

  .envelope { left: 266px; top: 672px; width: 434px; height: 203px; }
  .envelope .header { position: absolute; left: 18px; top: 20px; display: flex; align-items: center; gap: 5px; }
  .envelope .brand { font-size: 10px; }
  .envelope .dot { width: 10px; height: 10px; }
  .envelope .address { position: absolute; left: 18px; top: 40px; font-size: 5px; }

  .envelope-back { left: 736px; top: 672px; width: 444px; height: 203px; }
  .envelope-back .web { position: absolute; left: 0; right: 0; top: 24px; text-align: center; font-size: 7px; letter-spacing: 2px; color: #ffffff; }
</style>
</head>
<body>

  <section class="sheet letterhead">
    <svg class="swoosh" width="180" height="140" viewBox="0 0 180 140">
      <path d="M20 0 Q120 10 180 120 L180 0 Z" fill="var(--grey)"/>
      <path d="M40 0 Q130 8 180 100 L180 0 Z" fill="var(--teal)"/>
    </svg>
    <div class="header"><span class="dot" style="width:12px;height:12px"></span><span class="brand">Brightmoor Consulting Group</span></div>
    <div class="faint-circle"></div>
    <div class="contact small">
      27 Quillhaven Road, Suite 410<br>
      Port Washington, New York 11783<br>
      Tel (516) 555-0142<br>
      Fax (516) 555-0143<br>
      brightmoorconsulting.com
    </div>
  </section>

  <section class="sheet folder">
    <svg class="swoosh" width="190" height="190" viewBox="0 0 190 190">
      <path d="M10 0 Q130 20 190 175 L190 0 Z" fill="var(--grey)"/>
      <path d="M35 0 Q140 18 190 150 L190 0 Z" fill="var(--teal)"/>
    </svg>
    <div class="lockup">
      <span class="dot"></span>
      <span class="brand">Brightmoor<br>Consulting Group</span>
    </div>
  </section>

  <section class="sheet card card-front">
    <svg class="swoosh" width="70" height="50" viewBox="0 0 70 50">
      <path d="M5 0 Q50 6 70 45 L70 0 Z" fill="var(--grey)"/>
      <path d="M14 0 Q54 5 70 36 L70 0 Z" fill="var(--teal)"/>
    </svg>
    <div class="header"><span class="dot"></span><span class="brand">Brightmoor Consulting Group</span></div>
    <div class="details small">
      Mark Dellinger, President<br>
      27 Quillhaven Road, Suite 410<br>
      Port Washington, New York 11783<br>
      mdellinger@brightmoorconsulting.com
    </div>
    <div class="web">brightmoorconsulting.com</div>
  </section>

  <section class="sheet card card-back">
    <div class="faint-circle"></div>
  </section>

  <section class="sheet envelope">
    <svg class="swoosh" width="120" height="80" viewBox="0 0 120 80">
      <path d="M10 0 Q85 8 120 72 L120 0 Z" fill="var(--grey)"/>
      <path d="M24 0 Q92 6 120 58 L120 0 Z" fill="var(--teal)"/>
    </svg>
    <div class="header"><span class="dot"></span><span class="brand">Brightmoor Consulting Group</span></div>
    <div class="address small">27 Quillhaven Road, Suite 410, Port Washington, New York 11783</div>
  </section>

  <section class="sheet envelope-back">
    <svg width="444" height="70" viewBox="0 0 444 70" style="position:absolute;top:0;left:0">
      <path d="M0 30 Q0 62 40 62 L444 62 L444 0 L0 0 Z" fill="var(--grey)"/>
      <path d="M0 22 Q0 54 40 54 L444 54 L444 0 L0 0 Z" fill="var(--teal)"/>
    </svg>
    <div class="web">WWW.BRIGHTMOORCONSULTING.COM</div>
  </section>

</body>
</html>
```